magcian / mentalist needs flyer desined to send potentisl clients

I need a design that's contemporary, sharp, fun, and professional that will get the attention of whoever receives the flyer very quickly. This is for a tri-fold flyer design.

I've been performing magic for over 40 years. I've performed close-up,
parlor, and stage shows. I've been an Master of Ceremonies, Key Note
Speaker (using magic during presentations to help build on a point or
topic, while keeping the audience entertained and educated on the topic or
topics the client has asked me to focus). I've worked trade shows and
sales training incorporating magic as well. I did private shows in Las
Vegas and L.A. back in the late 90's as well.

I do have website / wesleytorvandmagic.example for your to check out.

Target Market(s)

The target audience is corporation Event Planners, Marketing and Sales
managers, casino & hotel entertainment directors, as well as private
businesses looking for unique entertainment options.

Industry/Entity Type

Entertainment Industry

Logo Text

Here are a couple of ideas: your mind is my playground, neural entertainer, professor of mysteries, master of your mind

Requirements
Must have
• I like the black and white look (I think it looks nice, but open to other
• ideas and creativity. Being I'm a magician and mentalist, I'd like for
• both venues to be conveyed somehow. My magic is clean and corporate and family friendly.
Nice to have
• I do have website / wesleytorvandmagic.example for your to check out.
• My current business card is attached for review. I'll also attach photos
• I'd like to share, but was unable when I last attempted do sign up. Some
• of the files were too big and I'm not savvy enough to make them smaller,
• but think there might be some potential with a couple.
Should not have
• cartoons or cartoonish graphics. no rabbits, doves, magicians, wands, or top hats.

```html
<!DOCTYPE html>
<html lang="en">
<head>
<meta charset="utf-8">
<title>Wesley Torvand – Tri-fold Flyer</title>
<link rel="stylesheet" href="https://fonts.googleapis.com/css2?family=Cormorant+Garamond:wght@500;600;700&family=Roboto:wght@300;700&family=Questrial&display=swap">
<style>
  :root {
    --paper: #fcfcfc;
    --ink: #111111;
    --body: #333333;
    --heading-blue: #1f2a3a;
    --shade: #e6e6e6;
    --illus-light: #d8dbda;
    --illus-dark: #3a3a3a;
  }
  * { margin: 0; padding: 0; box-sizing: border-box; }
  html, body { width: 1200px; height: 848px; overflow: hidden; background: var(--paper); }
  .flyer { position: relative; width: 1200px; height: 848px; background: var(--paper); color: var(--ink); overflow: hidden; }

  /* Left panel */
  .corner-shade {
    position: absolute; left: 0; top: 0; width: 420px; height: 128px;
    background: linear-gradient(180deg, var(--shade), var(--paper));
    clip-path: polygon(0 0, 100% 0, 70% 100%, 0 100%);
  }
  .corner-card {
    position: absolute; background: linear-gradient(135deg, #ffffff, #cfcfcf 60%, #2a2a2a);
    border: 2px solid var(--ink);
  }
  .corner-card--king { left: -30px; top: -70px; width: 110px; height: 160px; transform: rotate(-45deg); }
  .corner-card--diamond { left: 210px; top: -110px; width: 110px; height: 160px; transform: rotate(45deg); }

  .about { position: absolute; left: 50px; top: 142px; width: 316px; }
  .about__title {
    font-family: "Cormorant Garamond", serif; font-weight: 600; font-size: 31px;
    letter-spacing: 0.5px; text-align: center; margin-bottom: 16px; color: var(--ink);
  }
  .about__item {
    font-family: "Roboto", sans-serif; font-weight: 300; font-size: 14.4px;
    line-height: 22.8px; color: var(--body); margin-bottom: 22.8px;
  }
  .about__item strong { font-weight: 700; color: var(--ink); }

  /* Middle panel */
  .back-name {
    position: absolute; left: 440px; width: 320px; top: 430px; text-align: center;
    font-family: "Cormorant Garamond", serif; font-weight: 600; font-size: 24px; letter-spacing: 0.5px;
  }
  .contact { position: absolute; right: 442px; top: 696px; text-align: right; }
  .contact__pin { display: block; margin-left: auto; width: 32px; height: 42px; margin-right: 6px; }
  .contact__title {
    font-family: "Roboto", sans-serif; font-weight: 700; font-size: 15.5px;
    color: var(--heading-blue); margin-top: 8px; margin-bottom: 8px;
  }
  .contact__line { font-family: "Roboto", sans-serif; font-weight: 300; font-size: 14px; line-height: 19px; color: var(--body); }

  /* Front panel */
  .brand { position: absolute; left: 860px; width: 280px; top: 138px; text-align: center; }
  .brand__name {
    font-family: "Cormorant Garamond", serif; font-weight: 600; font-size: 31px; letter-spacing: 0.5px;
    padding-bottom: 4px; border-bottom: 1.5px solid var(--ink); display: inline-block;
  }
  .brand__tagline { font-family: "Questrial", sans-serif; font-size: 13.6px; letter-spacing: 0.4px; margin-top: 6px; }

  .card {
    position: absolute; left: 850px; top: 240px; width: 298px; height: 478px;
    border: 4px solid var(--ink); background: var(--paper);
  }
  .card__art {
    position: absolute; left: 6px; top: 6px; right: 6px; bottom: 6px;
    background: radial-gradient(ellipse at center, var(--illus-light) 0%, #9a9c9b 45%, var(--illus-dark) 75%, var(--paper) 76%);
  }
  .card__pip { position: absolute; width: 64px; height: 78px; fill: var(--ink); }
  .card__pip--top { left: 14px; top: 14px; }
  .card__pip--bottom { right: 18px; bottom: 14px; transform: rotate(180deg); }

  .index { position: absolute; text-align: center; font-family: "Cormorant Garamond", serif; font-weight: 500; font-size: 44px; line-height: 1; }
  .index svg { width: 24px; height: 30px; fill: var(--ink); display: block; margin: 4px auto 0; }
  .index--top { left: 806px; top: 228px; width: 40px; }
  .index--bottom { left: 1150px; top: 640px; width: 44px; }
  .index--bottom svg { margin: 0 auto 4px; }

  .studio { position: absolute; left: 849px; width: 300px; top: 745px; text-align: center; font-family: "Cormorant Garamond", serif; }
  .studio__name { font-weight: 600; font-size: 21px; letter-spacing: 0.6px; line-height: 1.1; }
  .studio__phone { font-weight: 700; font-size: 30px; line-height: 1.05; }
  .studio__web { font-weight: 700; font-size: 13.6px; }
</style>
</head>
<body>
<main class="flyer">
  <section class="panel panel--inside">
    <div class="corner-shade"></div>
    <div class="corner-card corner-card--king" role="img" aria-label="Illustrated king playing card, corner"></div>
    <div class="corner-card corner-card--diamond" role="img" aria-label="Illustrated king of diamonds playing card, corner"></div>

    <div class="about">
      <h2 class="about__title">ABOUT WESLEY</h2>
      <p class="about__item"><strong>I'm funny!</strong> You're guests will be laughing throughout the show guaranteeing a fun-filled experience!</p>
      <p class="about__item"><strong>I work clean.</strong> All of my comedy is corporate clean.</p>
      <p class="about__item"><strong>No cheesy tricks here.</strong> Your guests will experience magic that looks like magic.</p>
      <p class="about__item"><strong>I often tell people, “If magic really existed, this is what it would look like.”</strong> Your guests will experience magic exquisitely performed by a master of his craft.</p>
      <p class="about__item"><strong>I'm a professional entertainer.</strong> I've performed all over the country for major corporations which means you're getting tried and true, first-rate entertainment.</p>
      <p class="about__item"><strong>Doing business with me is easy.</strong> I make sure you're comfortable with every step in the process of dealing with me.</p>
      <p class="about__item"><strong>My performances are guaranteed!</strong> I pride myself on building relationships with my customers, so I'm not happy unless you're happy.</p>
    </div>
  </section>

  <section class="panel panel--back">
    <p class="back-name">WESLEY TORVAND</p>
    <div class="contact">
      <svg class="contact__pin" viewBox="0 0 32 42" aria-hidden="true">
        <path d="M16 0C7 0 0 7 0 16c0 11 16 26 16 26s16-15 16-26C32 7 25 0 16 0zm0 22a6 6 0 1 1 0-12 6 6 0 0 1 0 12z" fill="#111"/>
      </svg>
      <p class="contact__title">GET IN TOUCH</p>
      <p class="contact__line">wesleytorvandmagic@example.com</p>
      <p class="contact__line">505-555-0147</p>
    </div>
  </section>

  <section class="panel panel--front">
    <div class="brand">
      <p class="brand__name">WESLEY TORVAND</p>
      <p class="brand__tagline">Magician. Mentalist. Entertainer</p>
    </div>

    <div class="index index--top">W
      <svg viewBox="0 0 100 120" aria-hidden="true"><path d="M50 0C20 35 0 50 0 70c0 18 22 26 44 12l-8 38h28l-8-38c22 14 44 6 44-12 0-20-20-35-50-70z"/></svg>
    </div>

    <div class="card">
      <div class="card__art" role="img" aria-label="Line illustration of the performer in a vest and jacket, mirrored like a court playing card"></div>
      <svg class="card__pip card__pip--top" viewBox="0 0 100 120" aria-hidden="true"><path d="M50 0C20 35 0 50 0 70c0 18 22 26 44 12l-8 38h28l-8-38c22 14 44 6 44-12 0-20-20-35-50-70z"/></svg>
      <svg class="card__pip card__pip--bottom" viewBox="0 0 100 120" aria-hidden="true"><path d="M50 0C20 35 0 50 0 70c0 18 22 26 44 12l-8 38h28l-8-38c22 14 44 6 44-12 0-20-20-35-50-70z"/></svg>
    </div>

    <div class="index index--bottom">
      <svg viewBox="0 0 100 120" aria-hidden="true"><path d="M50 0C20 35 0 50 0 70c0 18 22 26 44 12l-8 38h28l-8-38c22 14 44 6 44-12 0-20-20-35-50-70z"/></svg>T
    </div>

    <div class="studio">
      <p class="studio__name">SLEIGHT LANE PRODUCTION</p>
      <p class="studio__phone">505.555.0147</p>
      <p class="studio__web">www.wesleytorvandmagic.example</p>
    </div>
  </section>
</main>
</body>
</html>
```